Business Card Design Project

We need a business card design for a management consultancy focused on financial innovation and digital money, run by experts from the Financial Services, Telecoms and Money Transfer industries.
Our products include services such as Mobile Payments, Mobile Money, Digital Wallets, Online Payments, Branchless Banking and more. We work with regulatory information, business plans, financial modelling, strategic planning, new products functional specification, new technologies evaluation, etc.
See company logo attached.
We would like to see 2 versions: one in portuguese and one in english (regarding data information). You can see below information needed (whenever there is a difference between the two versions, the first one is in english and the second one in portuguese).

Name
Position
Phone/ Tel: ++55-11-xxxx-xxxx
Cell/ Cel: ++55-11-9 xxxx-xxxx
Dr. Olavo Brendim Av., 312 - Tower II - 16th floor / Avenida Dr. Olavo Brendim, 312 - Torre II - 16o. andar
São Paulo - SP
06217-318 - Brazil/ 06217-318 - Brasil

Reason: 5 days to receive designs.

Target Market(s)

Audience: C-level executives from banks, credit card companies, acquirers, IT developers, retailers

Industry/Entity Type

Financial

Requirements
Must have
• Must use the logo and information above. Front must have white background. Back side should have only logo.
Nice to have
• Back should be in another colour but if it seems too exxagerated, maintain back in white also.
Should not have
• Do not add other illustrations to the business card.

```html
<!DOCTYPE html>
<html lang="en">
<head>
<meta charset="utf-8">
<title>Veltrano Management Consulting – Business Cards</title>
<link href="https://fonts.googleapis.com/css2?family=EB+Garamond:wght@400;600&display=swap" rel="stylesheet">
<style>
  :root {
    --page-bg: #e9eaec;
    --card-white: #ffffff;
    --navy-deep: #0d1c45;
    --navy-mid: #1d3a78;
    --steel-light: #9fdcee;
    --ink-navy: #0b1a3c;
    --name-blue: #1f3a8a;
    --text-grey: #4a4a4a;
    --rule-blue: #2f4fa8;
    --card-shadow: 0 6px 18px rgba(0, 0, 0, 0.18);
  }
  * { box-sizing: border-box; margin: 0; padding: 0; }
  html, body {
    width: 1200px;
    height: 1000px;
    overflow: hidden;
    background: var(--page-bg);
    font-family: "EB Garamond", Georgia, serif;
  }
  .sheet {
    width: 1200px;
    height: 1000px;
    display: flex;
    align-items: center;
    justify-content: center;
    gap: 50px;
  }
  .card {
    width: 540px;
    height: 310px;
    border-radius: 4px;
    box-shadow: var(--card-shadow);
    position: relative;
    overflow: hidden;
  }

  /* Back: brand side */
  .card--brand {
    background: linear-gradient(to bottom,
      var(--navy-deep) 0%,
      var(--navy-mid) 30%,
      var(--steel-light) 50%,
      var(--navy-mid) 70%,
      var(--navy-deep) 100%);
    display: flex;
    align-items: center;
    justify-content: center;
  }
  .brand {
    display: flex;
    align-items: center;
    gap: 16px;
    color: var(--ink-navy);
  }
  .brand__mark {
    width: 34px;
    height: 34px;
    background: var(--ink-navy);
  }
  .brand__name {
    font-weight: 400;
    text-transform: uppercase;
    line-height: 1.05;
  }
  .brand__name-main {
    display: block;
    font-size: 44px;
    letter-spacing: 2px;
  }
  .brand__name-sub {
    display: block;
    font-size: 18px;
    letter-spacing: 2.5px;
  }

  /* Front: contact side */
  .card--contact {
    background: var(--card-white);
    padding: 34px 30px 0;
    text-align: center;
    color: var(--text-grey);
  }
  .contact__name {
    font-size: 22px;
    font-weight: 600;
    color: var(--name-blue);
  }
  .contact__position {
    font-size: 13px;
    margin-top: 2px;
    color: #777;
  }
  .contact__phones {
    margin-top: 26px;
    font-size: 19px;
    line-height: 1.3;
    color: #3c3c3c;
  }
  .contact__addresses {
    margin-top: 26px;
    display: flex;
    justify-content: center;
    align-items: stretch;
    font-size: 14px;
    line-height: 1.3;
  }
  .address {
    width: 220px;
  }
  .address--en { text-align: right; padding-right: 14px; }
  .address--pt { text-align: left; padding-left: 14px; }
  .address-rule {
    width: 1px;
    background: var(--rule-blue);
  }
</style>
</head>
<body>
  <main class="sheet">
    <section class="card card--brand" aria-label="Business card back">
      <div class="brand">
        <span class="brand__mark" aria-hidden="true"></span>
        <span class="brand__name">
          <span class="brand__name-main">Veltrano</span>
          <span class="brand__name-sub">Management Consulting</span>
        </span>
      </div>
    </section>

    <section class="card card--contact" aria-label="Business card front">
      <h1 class="contact__name">Daniel Moreira</h1>
      <p class="contact__position">Position</p>
      <div class="contact__phones">
        <p>Phone/ Tel: ++55-11-xxxx-xxxx</p>
        <p>Cell/ Cel: ++55-11-9 xxxx-xxxx</p>
      </div>
      <div class="contact__addresses">
        <address class="address address--en" style="font-style:normal">
          Dr. Olavo Brendim Av., 312<br>
          Tower II - 16th floor<br>
          São Paulo - SP<br>
          06217-318 - Brazil
        </address>
        <span class="address-rule" aria-hidden="true"></span>
        <address class="address address--pt" style="font-style:normal">
          Avenida Dr. Olavo Brendim, 312<br>
          Torre II - 16o. andar<br>
          São Paulo - SP<br>
          06217-318 - Brasil
        </address>
      </div>
    </section>
  </main>
</body>
</html>
```